Beauty Salon Industry - Web Design Project

zQuarta is a well-funded start up developing an Online Marketing Platform for small businesses in Europe.
We require a large number of high quality business web designs for our business website builder. Our business websites are seamlessly integrated into our Online Marketing systems and therefore it is important for designers to comply with our Design Guidelines.
This is our second contest and it will focus on the beauty salon industry. We will be running contents every 2-3 weeks for a new industry. Last month, we ran a contest for Builder website designs with 3 top prizes (plus £10 per variation) and we also paid out £25 per design for 20+ entries from designers who did not win the top prizes. So we encourage all entries!
We have included a wire frame this time to encourage you to be as creative as possible with your designs and layout while respecting the following guidelines:
1) You CAN change the layout as much as you like. If you think a vertical menu would look better, then use it. If you think the design would benefit from moving an element to a different location, then you can do that too.
2) You must include ALL the elements in the wire frame in your design.(e.g. latest 2 news entries, a testimonial, 1 gallery image, carousel etc...). Please make sure you have looked through the wire frame and know what is required. Entries that do not include all the elements will not qualify to win.
3) So remember, you CAN change the layout as much as you like but DO NOT remove any elements nor move them to a different page.
4) You may change the size and style of the carousel image. We would like to see as many variations of this as possible.
We are rewarding 3 prizes, and would like the winning designer to design the internal pages to the new design.
As always, if we think your designs could be incorporated into our system, but you do not win the competition, we will reward £25. Therefore, we encourage designers to submit as many designs as possible as we may award up to 25 designs.
Judging criteria : -
1) Visual Design
2) Layout must adhere to best practices and wireframe. If you decide to move elements around significantly please provide reason
3) Functional, informative and drives calls to action
Updates
As usual:
1st place = £350
2nd place = £250
3rd place = £150
Good luck!
Very happy with all the designs submitted so far, and will provide feedback ASAP.
We would like to see you try arranging the elements differently. So please try different navigation types and layouts.
Thanks
Morris
Prize funds for 1st place has been slightly increased.
Thanks
Morris
We have already had some amazing designs submitted. Thanks.
Remember to play with the layout of the elements and try designs with a carousel/slider that is in portrait not just in landscape.
Thanks everyone!
Morris
Hi everyone, we are really enjoying looking through the designs.
We have one NEW requirement. If you have used an image from http://www.frelik-example.com/ in your design, could you please replace it with another.
We are not associated with them.
Thank you.
I have just sent a poll around the office to vote on all the designs and hope to have the results soon.
Good luck and I hope to see all your great designs for our next project in a couple of weeks.
Morris
Hi everyone, we hope you have had a good holiday season. We will be rewarding the prizes very soon, hopefully today or tomorrow.
Thanks
Morris
We are currently going through all the designs that did not win our competition and will be contacting the designers of the designs we would like to use in our system, so please keep an eye on your inbox over the next few days.
Thank you
Morris
Target Market(s)
Beauty Salon Industry
Industry/Entity Type
Beauty Salon
Look and feel
Each slider illustrates characteristics of the customer's brand and the style your logo design should communicate.

```html
<!DOCTYPE html>
<html lang="en">
<head>
<meta charset="utf-8">
<title>Velvet Lane – Hair and Urban Spa</title>
<link rel="stylesheet" href="https://fonts.googleapis.com/css2?family=Lato:wght@300;400;700&display=swap">
<style>
:root{
  --bg-dark:#2a0a17;
  --bg-mid:#5a1a33;
  --bg-light:#8c3d58;
  --wine:#6b1f3d;
  --wine-deep:#3d0f22;
  --rose:#b4607c;
  --rose-soft:#c77a92;
  --rose-text:#9a3d5c;
  --button:#b25574;
  --pink-panel:#f7e6ea;
  --pink-border:#e3c3cc;
  --ink:#333;
  --grey:#7a7a7a;
  --white:#fff;
}
*{margin:0;padding:0;box-sizing:border-box}
html,body{width:1200px;height:960px;overflow:hidden}
body{
  font-family:"Lato",Arial,sans-serif;
  position:relative;
  background:
    radial-gradient(ellipse 520px 700px at 1050px 350px,rgba(200,120,150,.55),transparent 70%),
    linear-gradient(90deg,var(--bg-dark) 0%,var(--bg-mid) 45%,var(--bg-light) 100%);
}
.abs{position:absolute}
.btn{position:absolute;display:flex;align-items:center;justify-content:center;color:var(--white);background:var(--button);font-size:11px;border:1px solid rgba(255,255,255,.4)}
.btn-dark{background:var(--wine-deep);font-size:15px;font-weight:700;border:1px solid rgba(255,255,255,.25)}

/* header */
.brand-mark{left:161px;top:25px;width:61px;height:61px;background:var(--rose-soft)}
.brand-name{left:241px;top:20px;font-size:45px;font-weight:400;color:var(--white);letter-spacing:.5px}
.brand-tag{left:242px;top:67px;font-size:15px;color:var(--white)}
.phone{right:148px;top:31px;font-size:26px;font-weight:300;color:var(--white)}
.book-now{left:960px;top:64px;width:94px;height:28px}

.nav{left:158px;top:119px;display:flex;gap:0;list-style:none}
.nav li{font-size:17px;color:#ead0d8;margin-right:30px}
.nav li.current{color:var(--white)}

/* hero */
.hero{left:137px;top:157px;width:926px;height:346px;background:linear-gradient(180deg,#3e1024 0%,#4d1630 60%,#5c1d39 100%)}
.hero-right{left:825px;top:157px;width:238px;height:346px;background:linear-gradient(180deg,#7e3550,#6a2743)}
.hero-title{left:151px;top:190px;width:230px;font-size:24px;line-height:27px;font-weight:300;color:var(--rose-soft)}
.hero-copy{left:154px;top:285px;width:180px;font-size:11px;line-height:13.6px;color:var(--rose-soft)}
.hero-copy p{margin-bottom:8px}
.hero-read{left:270px;top:452px;width:78px;height:21px}
.flap-left{left:374px;top:157px;width:85px;height:337px;background:linear-gradient(90deg,#6e2b46,#8a4560)}
.flap-right{left:741px;top:157px;width:83px;height:337px;background:linear-gradient(90deg,#8a4560,#6e2b46)}
.slider-frame{left:459px;top:157px;width:282px;height:373px;background:var(--wine-deep)}
.slide{left:468px;top:166px;width:263px;height:316px;background:radial-gradient(ellipse at 45% 40%,#a3324f,#6b1d33 55%,#3a0d1c)}
.dots{left:487px;top:500px;display:flex;gap:14px}
.dots span{width:12px;height:12px;border:1px solid #c98aa0}
.dots span.on{background:#c98aa0}
.price{left:859px;top:210px;font-size:60px;font-weight:700;color:#a54e6c}
.offer{left:857px;top:296px;width:190px;font-size:24px;line-height:27px;font-weight:700;color:#b06680}
.appt{left:850px;top:406px;width:193px;height:28px}

/* content */
.content{left:137px;top:503px;width:926px;height:294px;background:#e8dde0}
.content-inner{left:141px;top:507px;width:918px;height:286px;background:var(--white)}
.gallery-img{left:155px;top:515px;width:193px;height:228px;border:1px solid #ccc;background:linear-gradient(135deg,#d8d4d2,#8e7e7a 55%,#5a3d36)}
.view-more{left:270px;top:759px;width:78px;height:21px}
.quote{left:389px;top:551px;width:430px;font-size:13px;line-height:16px;color:var(--ink)}
.quote-name{left:392px;top:593px;font-size:13px;color:#555}
.quote-read{left:734px;top:593px;width:78px;height:21px}
.news{left:374px;top:631px;width:450px;height:151px;background:var(--pink-panel);border:1px solid var(--pink-border)}
.news-item{position:absolute;top:12px;width:200px}
.news-item .date{font-size:11px;color:#666}
.news-item h3{font-size:15px;font-weight:400;color:var(--rose-text);margin:3px 0 8px}
.news-item p{font-size:11px;line-height:17px;color:var(--grey)}
.more-news{left:734px;top:759px;width:78px;height:21px}
.side-title{left:858px;top:522px;font-size:15px;font-weight:700;color:var(--rose-text)}
.address{left:858px;top:545px;font-size:13px;line-height:20px;color:var(--grey)}
.view-map{left:857px;top:594px;width:79px;height:21px}
.side-rule{left:845px;top:633px;width:214px;height:1px;background:#ddd}
.hours-title{left:861px;top:651px;font-size:15px;font-weight:700;color:var(--rose-text)}
.hours{left:861px;top:676px;font-size:11px;line-height:17px;border-collapse:collapse}
.hours td:first-child{color:var(--grey);width:38px}
.hours td{color:#333}

/* partner strip */
.partners{left:137px;top:804px;width:926px;height:103px;background:linear-gradient(180deg,#fff,#f1f1f1 50%,#fff);display:flex;align-items:center;justify-content:space-around}
.partners span{font-size:30px;font-weight:400;color:#444}

/* footer */
.footer{left:825px;top:919px;width:238px;height:26px;background:#3a1424;display:flex;align-items:center;justify-content:space-between;padding:0 10px 0 11px}
.footer small{font-size:10px;color:#ddd}
.admin{background:#2a0c18;color:var(--white);font-size:11px;padding:3px 8px}
</style>
</head>
<body>
<header>
  <div class="abs brand-mark"></div>
  <div class="abs brand-name">VELVET LANE</div>
  <div class="abs brand-tag">Hair and Urban Spa</div>
  <div class="abs phone">020 7946 0321</div>
  <div class="btn btn-dark book-now">Book Now</div>
  <ul class="abs nav">
    <li class="current">Home</li><li>Services</li><li>Gallery</li><li>Testimonials</li><li>News</li><li>About Us</li><li>Contact Us</li>
  </ul>
</header>

<section>
  <div class="abs hero"></div>
  <div class="abs hero-right"></div>
  <h1 class="abs hero-title">LET OUR HAIR AND BEAUTY SKILLS BLOW YOU AWAY</h1>
  <div class="abs hero-copy">
    <p>Velvet Lane is a passionate, creative team, dedicated to delivering a second to none, personal salon experience that will 'blow' your mind.</p>
    <p>Where ultimate hairdressing comes hand-in-hand with style, glamour, fashion, innovation and skill to create an exquisite salon expperience in theheart of London</p>
  </div>
  <div class="btn hero-read">Read More</div>
  <div class="abs flap-left"></div>
  <div class="abs flap-right"></div>
  <div class="abs slider-frame"></div>
  <div class="abs slide" role="img" aria-label="Carousel photo of a woman with long glossy red hair"></div>
  <svg class="abs" style="left:410px;top:306px" width="20" height="38" aria-hidden="true"><polyline points="18,2 2,19 18,36" fill="none" stroke="#e8c9d4" stroke-width="1.5"/></svg>
  <svg class="abs" style="left:765px;top:306px" width="20" height="38" aria-hidden="true"><polyline points="2,2 18,19 2,36" fill="none" stroke="#e8c9d4" stroke-width="1.5"/></svg>
  <div class="abs dots"><span class="on"></span><span></span><span></span><span></span><span></span><span></span><span></span><span></span><span></span></div>
  <div class="abs price">£25</div>
  <div class="abs offer">Complimentary gift for first-time clients!</div>
  <div class="btn btn-dark appt">Book Appointment Now</div>
</section>

<main>
  <div class="abs content"></div>
  <div class="abs content-inner"></div>
  <div class="abs gallery-img" role="img" aria-label="Gallery photo of a woman with long straight brown hair"></div>
  <div class="btn view-more">View More</div>
  <p class="abs quote">"My hairstylist, noelle, was truly amazing. She listened to exactly what I wanted, but also told me exactly what ..."</p>
  <div class="abs quote-name">Maren Olsted</div>
  <div class="btn quote-read">Read More</div>
  <div class="abs news">
    <article class="news-item" style="left:12px">
      <div class="date">1 dec 2011</div>
      <h3>Book Now For Christmas</h3>
      <p>Our salon is usually very busy for the two weeks before Christmas, so please book early: call 020 7946 0321, or contact us.</p>
    </article>
    <article class="news-item" style="left:237px">
      <div class="date">9 nov 2011</div>
      <h3>Want to be hair model?</h3>
      <p>We always need models for our portfolio. If you want to become one please contact us.</p>
    </article>
  </div>
  <div class="btn more-news">More News</div>
  <div class="abs side-title">VELVET LANE</div>
  <div class="abs address">12 Marlow Place<br>London&nbsp; W1X 4QT</div>
  <div class="btn view-map">View Map</div>
  <div class="abs side-rule"></div>
  <div class="abs hours-title">Business Hours</div>
  <table class="abs hours">
    <tr><td>Mon.</td><td>9 a.m - 5 p.m.</td></tr>
    <tr><td>Tue.</td><td>9 a.m - 5 p.m.</td></tr>
    <tr><td>Wed.</td><td>9 a.m - 5 p.m.</td></tr>
    <tr><td>Thu.</td><td>9 a.m - 5 p.m.</td></tr>
    <tr><td>Fri.</td><td>9 a.m - 5 p.m.</td></tr>
    <tr><td>Sat.</td><td>9 a.m - 5 p.m.</td></tr>
  </table>
</main>

<div class="abs partners">
  <span>Lumeren</span><span>Vessa</span><span>Pine and pine</span><span>Halvorsen</span>
</div>

<footer class="abs footer">
  <small>Managed by zQuarta.com</small>
  <span class="admin">Admin</span>
</footer>
</body>
</html>
```